Wine Label front and back- Need to have an eye catching, classy wine label for restaurant placement.

label design for a wine label. eye catching for shelf placement. looking for simple and elegant label. Name of the vineyard will be the label recognition. Need back label to match with coloring and basic regulated info required by gov't (producer, address, and statement) Back label will be addressed after selected front label to match.
Will add $100 extra for the back label to match.

Target Market(s)

40-65 year old foodies

Colors
0355a3
eaf1f7

Requirements
Must have
• FERNHOLLOW (label name)
Estate,
Red Wine Blend NV,

```html
<!DOCTYPE html>
<html lang="en">
<head>
<meta charset="UTF-8">
<title>Fernhollow Estate – Red Wine Blend NV</title>
<link rel="stylesheet" href="https://fonts.googleapis.com/css2?family=Cormorant+Garamond:wght@400;500&display=swap">
<style>
  :root {
    --backdrop: #e6e6e6;
    --label-paper: #ffffff;
    --wine-red: #c8353c;
    --ink-grey: #6f6f6f;
    --rule-grey: #9a9a9a;
    --sketch-top: #f3f3f3;
    --sketch-bottom: #e4e4e4;
  }
  * { margin: 0; padding: 0; box-sizing: border-box; }
  html, body {
    width: 1127px;
    height: 1200px;
    overflow: hidden;
    background: var(--backdrop);
  }
  .canvas {
    position: relative;
    width: 1127px;
    height: 1200px;
  }
  .front-label {
    position: absolute;
    left: 307px;
    top: 50px;
    width: 513px;
    height: 1100px;
    background: var(--label-paper);
    font-family: "Cormorant Garamond", "Times New Roman", serif;
    text-align: center;
  }
  .street-sketch {
    position: absolute;
    left: 72px;
    top: 120px;
    width: 369px;
    height: 500px;
    display: block;
  }
  .estate-name {
    position: absolute;
    left: 0;
    right: 0;
    top: 668px;
    color: var(--wine-red);
    font-size: 42px;
    font-weight: 500;
    letter-spacing: 0.14em;
    line-height: 1;
  }
  .name-rule {
    position: absolute;
    left: 45px;
    top: 744px;
    width: 426px;
    height: 1px;
    background: var(--rule-grey);
  }
  .origin-statement {
    position: absolute;
    left: 0;
    right: 0;
    top: 774px;
    color: var(--ink-grey);
    font-size: 22px;
    letter-spacing: 0.1em;
    line-height: 34px;
    text-transform: uppercase;
  }
  .wine-details {
    position: absolute;
    left: 0;
    right: 0;
    top: 890px;
    color: var(--ink-grey);
    font-size: 24px;
    letter-spacing: 0.06em;
    line-height: 36px;
  }
  .volume {
    position: absolute;
    left: 0;
    right: 0;
    top: 1012px;
    color: var(--wine-red);
    font-size: 18px;
    letter-spacing: 0.04em;
  }
</style>
</head>
<body>
  <main class="canvas">
    <section class="front-label">
      <svg class="street-sketch" role="img" aria-label="Pencil sketch of a narrow cobbled village lane between old stone houses" viewBox="0 0 369 500" preserveAspectRatio="none">
        <defs>
          <linearGradient id="sketch-tone" x1="0" y1="0" x2="0" y2="1">
            <stop offset="0%" stop-color="var(--sketch-top)"/>
            <stop offset="100%" stop-color="var(--sketch-bottom)"/>
          </linearGradient>
        </defs>
        <rect width="369" height="500" fill="url(#sketch-tone)"/>
      </svg>

      <h1 class="estate-name">FERNHOLLOW</h1>
      <div class="name-rule"></div>

      <p class="origin-statement">Grown and bottled in<br>Fernhollow</p>

      <p class="wine-details">Estate<br>Red Wine Blend NV</p>

      <p class="volume">750 mls</p>
    </section>
  </main>
</body>
</html>
```